Brochure Design for Velmora Shoes- Online Shoe Retailer

Specialises in ladies shoes in larger sizes. Provides excellent customer service and a great range of shoes etc. Wide range.

```html
<!DOCTYPE html>
<html lang="en">
<head>
<meta charset="utf-8">
<title>Velmora Shoes – Winter Range Brochure</title>
<link rel="stylesheet" href="https://fonts.googleapis.com/css2?family=Questrial&family=Oswald:wght@500;700&family=Lato:ital,wght@1,400;1,700&display=swap">
<style>
  :root {
    --paper: #f6f4ee;
    --tile: #fcfbf8;
    --grid-line: #e6dfcf;
    --label-bg: #e0dacb;
    --blank-bar: #ebe6da;
    --brand-red: #8a3633;
    --ink: #1d1b1a;
    --muted: #9a7f76;
    --logo-bg: #161515;
    --logo-accent: #e9a48a;
    --white: #ffffff;
  }
  html, body { margin: 0; padding: 0; overflow: hidden; background: var(--paper); }
  .canvas {
    position: relative; width: 1200px; height: 848px; overflow: hidden;
    background: var(--paper);
    font-family: "Questrial", "Century Gothic", sans-serif;
  }
  .stage { position: absolute; left: 0; top: 0; width: 900px; height: 636px; transform: scale(1.33333); transform-origin: 0 0; }
  .diagonal { position: absolute; left: 0; top: 0; width: 0; height: 0; transform: rotate(-45deg); transform-origin: 0 0; }

  .grid-line { position: absolute; background: var(--grid-line); }
  .grid-line.row { height: 1px; left: -900px; width: 2200px; }
  .grid-line.col { width: 1px; top: -200px; height: 1500px; }

  .product { position: absolute; width: 178px; height: 185px; }
  .product .tile {
    position: absolute; left: 10px; top: 4px; width: 136px; height: 140px;
    background: var(--tile); box-shadow: 0 0 6px rgba(120, 100, 70, 0.12);
  }
  .product .photo { position: absolute; left: 22px; top: 18px; width: 112px; height: 96px; border-radius: 10px; }
  .product .side-bar { position: absolute; left: 150px; top: 14px; width: 24px; height: 118px; background: var(--blank-bar); }
  .product .price-tag {
    position: absolute; left: 22px; top: 156px; width: 118px; height: 26px;
    background: var(--label-bg); display: flex; align-items: center; justify-content: center; gap: 4px;
    font-size: 8.5px; letter-spacing: 0.4px; white-space: nowrap;
  }
  .price-tag .name { color: var(--muted); text-transform: uppercase; }
  .price-tag .price { color: var(--ink); font-weight: 700; }

  .logo-block {
    position: absolute; left: -150px; top: 176px; width: 150px; height: 96px;
    background: var(--logo-bg); display: flex; flex-direction: column; justify-content: center;
    padding-left: 14px; box-sizing: border-box; white-space: nowrap;
  }
  .logo-block .wordmark { display: flex; align-items: center; gap: 7px; color: var(--white); font-size: 17px; }
  .logo-block .mark { width: 10px; height: 10px; border-radius: 50%; background: var(--logo-accent); flex: none; }
  .logo-block .tagline { color: var(--logo-accent); font-size: 6.5px; margin-top: 5px; margin-left: 17px; }

  .stock-banner {
    position: absolute; left: -150px; top: 282px; width: 312px; height: 24px;
    background: var(--brand-red); color: var(--white);
    display: flex; align-items: center; justify-content: center; gap: 10px;
    font-size: 10.5px; letter-spacing: 0.6px; white-space: nowrap;
  }
  .stock-banner strong { font-family: "Oswald", sans-serif; font-weight: 500; letter-spacing: 1px; }

  .winter-callout {
    position: absolute; left: -150px; top: 520px; width: 120px;
    transform: rotate(63deg); transform-origin: center;
    font-family: "Oswald", "Arial Narrow", sans-serif; font-weight: 700;
    font-size: 20px; line-height: 19px; color: var(--brand-red); text-align: center;
  }
  .winter-callout .now { color: var(--ink); }

  .contact-note {
    position: absolute; left: 20px; top: 872px; width: 360px;
    font-family: "Lato", sans-serif; font-style: italic; font-size: 8.6px; line-height: 12px;
    color: var(--brand-red); white-space: nowrap;
  }
  .contact-note b { color: var(--ink); }
</style>
</head>
<body>
<div class="canvas">
  <div class="stage">
    <div class="diagonal">
      <div class="grid-line row" style="top:127px"></div>
      <div class="grid-line row" style="top:312px"></div>
      <div class="grid-line row" style="top:497px"></div>
      <div class="grid-line row" style="top:682px"></div>
      <div class="grid-line row" style="top:867px"></div>
      <div class="grid-line col" style="left:-348px"></div>
      <div class="grid-line col" style="left:-170px"></div>
      <div class="grid-line col" style="left:8px"></div>
      <div class="grid-line col" style="left:186px"></div>
      <div class="grid-line col" style="left:364px"></div>

      <div class="logo-block">
        <div class="wordmark"><span class="mark"></span><span>Velmora Shoes</span></div>
        <div class="tagline">Stylish shoes in larger sizes</div>
      </div>

      <div class="stock-banner"><span>LADIES SHOES SIZES 9-15</span><strong>NEW STOCK AVAILABLE</strong></div>

      <div class="product" style="left:-170px; top:312px">
        <div class="tile"><div class="photo" role="img" aria-label="Red patterned flat sandal" style="background:linear-gradient(135deg,#b5542c,#e3a0a8)"></div></div>
        <div class="side-bar"></div>
        <div class="price-tag"><span class="name">Carina Red</span><span class="price">$ 40.00</span></div>
      </div>
      <div class="product" style="left:8px; top:312px">
        <div class="tile"><div class="photo" role="img" aria-label="Black knee-high boots" style="background:linear-gradient(135deg,#111,#3b3b3b)"></div></div>
        <div class="side-bar"></div>
        <div class="price-tag"><span class="name">Elsa Black</span><span class="price">$ 150.00</span></div>
      </div>
      <div class="product" style="left:186px; top:312px">
        <div class="tile"><div class="photo" role="img" aria-label="Brown peep-toe wedge" style="background:linear-gradient(135deg,#a8794a,#dcc09a)"></div></div>
        <div class="side-bar"></div>
        <div class="price-tag"><span class="name">Mirren Brown</span><span class="price">$ 100.00</span></div>
      </div>

      <div class="winter-callout"><div>WINTER</div><div>RANGE</div><div class="now">NOW</div><div>ONLINE</div></div>

      <div class="product" style="left:8px; top:497px">
        <div class="tile"><div class="photo" role="img" aria-label="Brown buckled ankle boots" style="background:linear-gradient(135deg,#5e2c12,#a0592c)"></div></div>
        <div class="side-bar"></div>
        <div class="price-tag"><span class="name">Soho Brown</span><span class="price">$ 155.00</span></div>
      </div>
      <div class="product" style="left:186px; top:497px">
        <div class="tile"><div class="photo" role="img" aria-label="Teal strappy heels" style="background:linear-gradient(135deg,#137f95,#3cb6c9)"></div></div>
        <div class="side-bar"></div>
        <div class="price-tag"><span class="name">Odette</span><span class="price">$ 95.00</span></div>
      </div>

      <div class="product" style="left:8px; top:682px">
        <div class="tile"><div class="photo" role="img" aria-label="Snake print flats" style="background:linear-gradient(135deg,#b7a984,#e4dcc4)"></div></div>
        <div class="side-bar"></div>
        <div class="price-tag"><span class="name">Vienna Snake</span><span class="price">$ 90.00</span></div>
      </div>
      <div class="product" style="left:186px; top:682px">
        <div class="tile"><div class="photo" role="img" aria-label="Mint thong sandal" style="background:linear-gradient(135deg,#2f6b45,#4c3a2c)"></div></div>
        <div class="side-bar"></div>
        <div class="price-tag"><span class="name">Coast Mint</span><span class="price">$ 80.00</span></div>
      </div>

      <div class="contact-note">
        <div>Visit us online today at <b>www.velmorashoes.com.au</b> to see our full range</div>
        <div>Phone and Email orders welcome: 07 5550 1234 - sales@velmorashoes.com.au</div>
        <div>Get 10% Off your next order</div>
        <div>simply enter code <b>VELMORA10</b> during checkout.</div>
      </div>
    </div>
  </div>
</div>
</body>
</html>
```